Paw Haven Postcard - Let People Know What Animal Chiropractic Is!

I am looking for a postcard someone can look at and know why their pet needs animal chiropractic and how they can schedule the appointment. I have included the old postcard, new photos to use and logo. The contact info that needs to go on this card:

www.pawhavenvet.com
510-555-0142
assistant.drmarlow@quillmail.com

QR code - https://www.vidtrove.com/list?id=QX8m2Rt5KdWpZ3nB7yLfHa9cVe

Target Market(s)

Pet owners

Industry/Entity Type

Animal Health Care - Chiropractic

Font styles to use
Sans Serif

Requirements
Must have
• Logo, contact info, reasons for a pet needing chiropractic care, PICTURES (who doesn't love pictures)
Nice to have
• A tiny blurb on what chiropractic is for animals.
Should not have
• Empty space for an address, this card will be handed out. I do not want it to look exactly like the old one. I don't want it to be so wordy.

```html
<!DOCTYPE html>
<html lang="en">
<head>
<meta charset="utf-8">
<title>Paw Haven Postcard</title>
<link href="https://fonts.googleapis.com/css2?family=Anton&family=Oswald:wght@600&family=Poppins:wght@400;500;600;700;800&display=swap" rel="stylesheet">
<style>
  :root{
    --red:#c01b2c;
    --dark:#363639;
    --grey:#bcbdbf;
    --light-grey:#d9d9db;
    --white:#ffffff;
    --ink:#2e2e31;
    --stage:#f4f4f4;
  }
  *{box-sizing:border-box;margin:0;padding:0}
  html,body{width:1200px;height:2534px;overflow:hidden;background:var(--stage)}
  body{position:relative;font-family:"Poppins",sans-serif;color:var(--ink)}
  .card{position:absolute;width:880px;height:588px;background:var(--white);overflow:hidden;box-shadow:0 12px 18px rgba(0,0,0,.22)}
  .card--front{left:170px;top:1157px}
  .card--back{left:170px;top:1818px}
  .shapes{position:absolute;left:0;top:0;width:880px;height:588px}
  .abs{position:absolute}

  .headline{left:38px;top:34px;line-height:1}
  .headline__top{font-family:"Anton",sans-serif;font-size:58px;color:var(--white);letter-spacing:-.5px;transform:scaleX(.92);transform-origin:left;white-space:nowrap}
  .headline__top span{color:var(--dark)}
  .headline__bottom{font-family:"Poppins",sans-serif;font-weight:800;font-size:45px;color:var(--white);margin-top:-4px;letter-spacing:.5px;white-space:nowrap}

  .badge{width:150px;text-align:center}
  .badge__certified{font-family:"Poppins",sans-serif;font-weight:500;font-size:26px;color:var(--white);letter-spacing:.5px}
  .badge__title{font-family:"Oswald",sans-serif;font-weight:600;font-size:15px;color:var(--white);line-height:32px;margin-left:-10px;width:170px;white-space:nowrap}

  .why{left:40px;top:198px;font-weight:700;font-size:21px;line-height:1.15;color:var(--ink);white-space:nowrap}
  .why span{display:block;color:var(--red)}
  .checklist{list-style:none;width:240px}
  .checklist li{position:relative;padding-left:33px;font-size:14px;line-height:16.5px;margin-bottom:5px;color:var(--ink);white-space:nowrap}
  .checklist li svg{position:absolute;left:0;top:2px;width:20px;height:16px}

  .band-label{font-weight:700;font-size:14.5px;color:var(--ink);white-space:nowrap}
  .band-label--red{color:var(--white)}
  .phone-block{display:flex;gap:8px;align-items:center;white-space:nowrap}
  .phone-icon{width:26px;height:26px;border-radius:6px;background:var(--red);display:flex;align-items:center;justify-content:center;flex:none}
  .phone-icon svg{width:16px;height:16px}
  .phone-block__num{font-weight:700;font-size:18px;color:var(--red);line-height:1}
  .phone-block__mail{font-size:13px;color:var(--ink);line-height:1.2}
  .note{font-size:14.5px;line-height:17px;color:var(--ink);white-space:nowrap}
  .note b{color:var(--red)}
  .web{font-size:15px;color:var(--ink);white-space:nowrap}
  .web b{color:var(--red);font-weight:700}

  .logo-ring{border-radius:50%;background:var(--light-grey);display:flex;align-items:center;justify-content:center}
  .logo-ring__inner{border-radius:50%;background:var(--white);display:flex;flex-direction:column;align-items:center;justify-content:center;gap:6px}
  .logo-ring__dot{width:14px;height:14px;border-radius:50%;background:var(--red)}
  .logo-ring__name{font-weight:700;font-size:11px;color:var(--ink);text-align:center;line-height:1.2}

  .what{left:42px;top:36px;width:418px;color:var(--white)}
  .what h2{font-weight:700;font-size:22px;margin-bottom:6px}
  .what p{font-size:14px;line-height:18.2px}
  .dark-band-text{left:148px;top:337px;color:var(--white);font-size:14.5px;line-height:18px;white-space:nowrap}
  .dark-band-text b{font-weight:700}
  .cred{left:40px;top:400px;font-weight:700;font-size:15px;color:var(--ink);white-space:nowrap}
  .cred span{color:var(--red)}
  .guild{left:42px;top:440px;font-size:16px;line-height:20px;color:var(--ink);white-space:nowrap}
  .guild b{display:block;color:var(--red);font-weight:700}
  .guild i{display:block;width:52px;height:3px;background:var(--ink);margin-top:8px}
  .schedule{left:42px;top:508px;font-weight:700;font-size:14.5px;line-height:17px;color:var(--ink);white-space:nowrap}
  .schedule span{display:block;color:var(--red)}
  .thumbs{left:308px;top:397px;display:flex;gap:8px}
  .thumb{width:133px;height:100px;border:2px solid var(--red);border-radius:3px}
</style>
</head>
<body>

<section class="card card--front">
  <svg class="shapes" viewBox="0 0 880 588">
    <defs>
      <linearGradient id="frontPhoto" x1="0" y1="0" x2="0" y2="1">
        <stop offset="0" stop-color="#6f9fd6"/>
        <stop offset=".35" stop-color="#8a8f95"/>
        <stop offset=".7" stop-color="#5b4d3e"/>
        <stop offset="1" stop-color="#4d7a3a"/>
      </linearGradient>
    </defs>
    <path d="M0 0H560V170Q300 175 0 195Z" fill="var(--red)"/>
    <path d="M880 600V520Q760 470 700 380Q650 290 640 170Q635 90 660 0H880Z" fill="var(--grey)"/>
    <path d="M880 540Q770 480 715 380Q670 290 668 170Q668 90 690 0H880Z" fill="url(#frontPhoto)" role="img" aria-label="Photo of the chiropractor crouching on a gravel path with two dogs"/>
    <path d="M0 483H300L292 503H0Z" fill="var(--grey)"/>
    <path d="M302 483H680L670 503H294Z" fill="var(--red)"/>
    <path d="M0 588V555Q380 560 880 540V588Z" fill="var(--grey)"/>
    <path d="M0 550Q380 555 880 520V530Q380 565 0 558Z" fill="var(--white)"/>
    <path d="M518 0H668V150L593 168L518 150Z" fill="var(--dark)"/>
    <path d="M510 74H676V106H510Z" fill="var(--red)"/>
    <path d="M510 106L518 114V106Z M676 106L668 114V106Z" fill="#7a0f1a"/>
  </svg>

  <div class="abs headline">
    <div class="headline__top">CHIROPRACTIC <span>CARE</span></div>
    <div class="headline__bottom">FOR YOUR PET</div>
  </div>

  <div class="abs badge" style="left:518px;top:36px">
    <div class="badge__certified">CERTIFIED</div>
    <div class="badge__title" style="margin-top:3px">ANIMAL CHIROPRACTOR</div>
  </div>

  <div class="abs why">WHY DOES MY PET NEED CHIROPRACTIC -<span>SIGNS | SYMPTOMS</span></div>

  <ul class="abs checklist" style="left:40px;top:267px">
    <li><svg viewBox="0 0 20 16"><path d="M2 8L8 14L18 2" fill="none" stroke="#c01b2c" stroke-width="3"/></svg>A limp that will not<br>go away</li>
    <li><svg viewBox="0 0 20 16"><path d="M2 8L8 14L18 2" fill="none" stroke="#c01b2c" stroke-width="3"/></svg>Yelping in pain with<br>sudden movement</li>
    <li><svg viewBox="0 0 20 16"><path d="M2 8L8 14L18 2" fill="none" stroke="#c01b2c" stroke-width="3"/></svg>Resists jumping in,<br>out or on things as much</li>
    <li><svg viewBox="0 0 20 16"><path d="M2 8L8 14L18 2" fill="none" stroke="#c01b2c" stroke-width="3"/></svg>Diagnosed with<br>disc disease</li>
    <li><svg viewBox="0 0 20 16"><path d="M2 8L8 14L18 2" fill="none" stroke="#c01b2c" stroke-width="3"/></svg>Wellness (Prevention) -<br>a well moving spine will help<br>prevent arthritis later in life</li>
  </ul>
  <ul class="abs checklist" style="left:290px;top:267px;width:270px">
    <li><svg viewBox="0 0 20 16"><path d="M2 8L8 14L18 2" fill="none" stroke="#c01b2c" stroke-width="3"/></svg>Rehab for sprain/strain,<br>surgery</li>
    <li><svg viewBox="0 0 20 16"><path d="M2 8L8 14L18 2" fill="none" stroke="#c01b2c" stroke-width="3"/></svg>Athletics - flyball, agility,<br>show dogs - top athletes<br>receive regular chiropractic care</li>
    <li><svg viewBox="0 0 20 16"><path d="M2 8L8 14L18 2" fill="none" stroke="#c01b2c" stroke-width="3"/></svg>Working Animals - Police,<br>service</li>
    <li><svg viewBox="0 0 20 16"><path d="M2 8L8 14L18 2" fill="none" stroke="#c01b2c" stroke-width="3"/></svg>Sudden change in behavior that<br>is unexplained</li>
    <li><svg viewBox="0 0 20 16"><path d="M2 8L8 14L18 2" fill="none" stroke="#c01b2c" stroke-width="3"/></svg>Hip pain</li>
  </ul>

  <div class="abs band-label" style="left:42px;top:485px">LOCATION BY APPOINTMENT</div>
  <div class="abs band-label band-label--red" style="left:318px;top:485px">DR. DANA MARLOW, CHIROPRACTOR,</div>

  <div class="abs phone-block" style="left:42px;top:512px">
    <div class="phone-icon"><svg viewBox="0 0 16 16"><path d="M4 1L6.5 4.5L5 6.5Q6.5 9.5 9.5 11L11.5 9.5L15 12L13 15Q6 14 1 3Z" fill="#fff"/></svg></div>
    <div><div class="phone-block__num">510-555-0142</div><div class="phone-block__mail">assistant.drmarlow@quillmail.com</div></div>
  </div>
  <div class="abs note" style="left:330px;top:512px">who has been providing chiropractic<br>care for over <b>15 years!</b></div>
  <div class="abs web" style="left:655px;top:542px">www.<b>pawhavenvet</b>.com</div>

  <div class="abs logo-ring" style="left:678px;top:370px;width:170px;height:170px">
    <div class="logo-ring__inner" style="width:148px;height:148px">
      <div class="logo-ring__dot"></div>
      <div class="logo-ring__name">DR. DANA MARLOW</div>
    </div>
  </div>
</section>

<section class="card card--back">
  <svg class="shapes" viewBox="0 0 880 588">
    <defs>
      <linearGradient id="backPhoto" x1="0" y1="0" x2="1" y2="1">
        <stop offset="0" stop-color="#a8a9a3"/>
        <stop offset=".5" stop-color="#c9c8c2"/>
        <stop offset="1" stop-color="#8d8f89"/>
      </linearGradient>
    </defs>
    <rect width="880" height="588" fill="var(--white)"/>
    <path d="M560 0H880V360H560Z" fill="url(#backPhoto)" role="img" aria-label="Photo of a small white bulldog in a pink wheelchair cart on a sidewalk"/>
    <path d="M0 0H620Q600 120 640 220Q690 320 880 320V400H0Z" fill="var(--red)"/>
    <path d="M640 220Q700 310 880 300V320Q690 320 640 220Z" fill="var(--grey)"/>
    <path d="M95 325H880V385H85L125 355Z" fill="var(--dark)"/>
    <path d="M0 395L95 325L90 395Z" fill="var(--red)"/>
    <path d="M0 398H290L280 420H0Z" fill="var(--grey)"/>
    <path d="M0 588V545Q420 560 880 525V588Z" fill="var(--grey)"/>
    <path d="M0 540Q300 560 600 560L0 568Z" fill="var(--red)"/>
    <path d="M468 0H618V145L543 163L468 145Z" fill="var(--dark)"/>
    <path d="M460 70H626V102H460Z" fill="var(--red)"/>
  </svg>

  <div class="abs what">
    <h2>WHAT IS CHIROPRACTIC</h2>
    <p>in simplest terms, a conservative approach to healthcare. We focus on the movement in the joints (spine/extremities) for the overall health &amp; wellness of the pet. Restrictions in joint motion, can affect such things as athletic performance, normal biomechanic leading to repetitive stress injuries &amp; sprain/strains. The issue, most restrictions in joint motions are subclinical &amp; go undetected until they manifest into a problem. Animal chiropractic adjustments are not only for pets with injuries, it's great to start young so that we know how the spine/ extremities are moving prior to a problem. Chiropractic adjustments definitely help with new and existing injuries. We also offer low level laser treatments to assist in the healing process.</p>
  </div>

  <div class="abs badge" style="left:468px;top:36px">
    <div class="badge__certified">CERTIFIED</div>
    <div class="badge__title" style="margin-top:2px">ANIMAL CHIROPRACTOR</div>
  </div>

  <div class="abs logo-ring" style="left:478px;top:158px;width:134px;height:134px">
    <div class="logo-ring__inner" style="width:116px;height:116px">
      <div class="logo-ring__dot"></div>
      <div class="logo-ring__name" style="font-size:9.5px">DR. DANA MARLOW</div>
    </div>
  </div>

  <div class="abs dark-band-text"><b>DR. DANA MARLOW, CHIROPRACTOR,</b><br>who has been providing chiropractic care for over <b>15 years!</b></div>

  <div class="abs cred"><span>DR. DANA</span> MARLOW, CCSP</div>
  <div class="abs guild">Global Animal<b>CHIROPRACTIC GUILD</b><i></i></div>
  <div class="abs schedule">SCHEDULE AN<span>APPOINTMENT TODAY</span></div>

  <div class="abs thumbs">
    <div class="thumb" style="background:linear-gradient(135deg,#5a4a3a,#b88a5c)" role="img" aria-label="Photo of the chiropractor adjusting a horse in a stable"></div>
    <div class="thumb" style="background:linear-gradient(135deg,#c8cdd6,#4f5a6e)" role="img" aria-label="Photo of the chiropractor treating a dog indoors"></div>
    <div class="thumb" style="background:linear-gradient(180deg,#6f9fd6,#6a6a66)" role="img" aria-label="Photo of the chiropractor outdoors with two dogs"></div>
    <div class="thumb" style="background:linear-gradient(135deg,#e6e6e6,#8a6e55)" role="img" aria-label="Photo of the chiropractor with a bulldog"></div>
  </div>

  <div class="abs phone-block" style="left:230px;top:508px">
    <div class="phone-icon"><svg viewBox="0 0 16 16"><path d="M4 1L6.5 4.5L5 6.5Q6.5 9.5 9.5 11L11.5 9.5L15 12L13 15Q6 14 1 3Z" fill="#fff"/></svg></div>
    <div><div class="phone-block__num">510-555-0142</div><div class="phone-block__mail" style="font-size:14.5px">assistant.drmarlow@quillmail.com</div></div>
  </div>
  <div class="abs web" style="left:592px;top:538px;font-size:18px">www.<b>pawhavenvet</b>.com</div>
</section>

</body>
</html>
```